Disability and mental health support work company requires business card

Specialising
Bellwind Disability is a new HVTA service aimed toward HVTA participants with a history of criminal justice, psychosocial/mental health, intellectual, and cognitive disabilities.

Our focus
Focusing on providing core HVTA supports for community participation, daily activities and supported independent living.

Authentic
Likeminded people wanting to make a difference in participant's lives.

Our aim to provide holistic and empowering supports targeted towards creating independence and guidance for all participants and families.
Over 35 years of experience working with people that have psychosocial, intellectual, and cognitive disabilities.

Industry/Entity Type

disability and mental health

Contact Information for Business Card

logo - business name

Colors
0054AA
0677BA
7BADD7
CADEEF
E8F1F8
FFF300
FFF600
FEFA6F
FFFEC7
FFFEE8

Requirements
Must have
• want double sided business cards(wont let me change it)
Should not have
• any disability related pictures

```html
<!DOCTYPE html>
<html lang="en">
<head>
<meta charset="utf-8">
<title>Bellwind Disability — Business Card</title>
<link rel="stylesheet" href="https://fonts.googleapis.com/css2?family=Poppins:ital,wght@0,300;0,400;0,600;1,400&display=swap">
<style>
  :root{
    --backdrop:#2b2b2b;
    --navy:#133a63;
    --navy-deep:#0d2c4d;
    --sky:#7aa6d2;
    --gold:#c9a227;
    --white:#f3f6fa;
  }
  *{margin:0;padding:0;box-sizing:border-box}
  html,body{width:1200px;height:1138px;overflow:hidden;background:var(--backdrop)}
  body{position:relative;font-family:"Poppins",sans-serif;color:var(--white)}

  .card{position:absolute;width:620px;height:375px;border-radius:16px;overflow:hidden;background:var(--navy)}
  .card--front{left:274px;top:186px}
  .card--back{left:276px;top:608px}

  /* front */
  .front-name{position:absolute;left:0;right:0;top:210px;text-align:center;
    font-weight:600;font-size:34px;letter-spacing:.06em;color:var(--navy-deep);text-transform:uppercase}
  .front-web{position:absolute;left:0;right:0;top:318px;text-align:center;
    font-weight:400;font-size:16px;letter-spacing:.42em;color:var(--white)}
  .front-web .accent{color:var(--gold)}

  /* back */
  .contact-panel{position:absolute;left:0;right:0;bottom:0;height:140px;background:var(--sky)}
  .contact-rule{position:absolute;left:0;right:0;top:231px;height:4px;background:var(--gold)}

  .holder{position:absolute;left:30px;top:50px}
  .holder-name{font-weight:600;font-size:24px;line-height:1.2;text-transform:uppercase;color:var(--white)}
  .holder-role{font-style:italic;font-size:16px;color:var(--gold);margin-top:1px}
  .holder-address{font-weight:300;font-size:16px;line-height:24px;margin-top:14px}

  .contacts{position:absolute;left:30px;top:264px;list-style:none}
  .contacts li{display:flex;align-items:center;height:25.5px;font-weight:400;font-size:16px;color:var(--white)}
  .contacts svg{width:16px;height:14px;margin-right:14px;flex:none}

  .brand-seal{position:absolute;left:384px;top:34px;width:180px;height:180px;border-radius:50%;
    border:3px solid var(--sky);display:flex;align-items:center;justify-content:center;text-align:center}
  .brand-seal span{font-weight:600;font-size:20px;line-height:1.25;letter-spacing:.05em;color:var(--sky);text-transform:uppercase}
</style>
</head>
<body>

<section class="card card--front" aria-label="Business card front">
  <p class="front-name">Bellwind Disability</p>
  <p class="front-web">www.bellwind<span class="accent">disability</span>.com</p>
</section>

<section class="card card--back" aria-label="Business card back">
  <div class="contact-rule"></div>
  <div class="contact-panel"></div>

  <div class="holder">
    <h1 class="holder-name">Owen Hartley</h1>
    <p class="holder-role">Managing Director</p>
    <p class="holder-address">58 Harbour Lane,<br>Fairview, US 204816</p>
  </div>

  <ul class="contacts">
    <li>
      <svg viewBox="0 0 16 14" aria-hidden="true"><path fill="#fff" d="M1 4c0-2 3-3 7-3s7 1 7 3v1h-4V4H5v1H1zM3 6h10l1 7H2z"/><circle cx="8" cy="9.5" r="1.8" fill="var(--sky)"/></svg>
      020-0303-0404
    </li>
    <li>
      <svg viewBox="0 0 16 14" aria-hidden="true"><rect x="1" y="2" width="14" height="10" fill="#fff"/><path d="M1 2l7 6 7-6M1 12l5-5M15 12l-5-5" stroke="var(--sky)" stroke-width="1.2" fill="none"/></svg>
      bellwinddisability.com
    </li>
    <li>
      <svg viewBox="0 0 16 14" aria-hidden="true"><circle cx="8" cy="7" r="6" fill="#fff"/><path d="M2 7h12M8 1v12M4 3.5q4 2 8 0M4 10.5q4-2 8 0" stroke="var(--sky)" stroke-width=".9" fill="none"/></svg>
      owen@bellwinddisability.com
    </li>
  </ul>

  <div class="brand-seal"><span>Bellwind<br>Disability</span></div>
</section>

</body>
</html>
```